Tuition Center Website

We need a new web site for a tutoring company based in sydney.

We only teach senior highschool students and pride ourselves on building the students abilities to think their way through life.

I would like a bright and vibrant website that looks professional and modern.
It needs to look simple and neat but also have the functionality we need.
Images and flash would be good.

Please keep in mind that the site must be appealing to a younger audience.

We need a multipage website with the following navigation bars:

1.Home (As logo not "home" button)
I would like a news box/ticker somewhere that can stream our chatterbook and flitter feeds and also any news updates we want to put up.
Subscribe to newsletter button.

2. About us.
This needs to be a pull down into:
-What we do
-Why we do it
-How we do it

3. Courses
Pulldown into:
-Maths
-English
-Science
(we may need to attach extra pages behind these e.g. Courses/Science/Physics or Courses/Science/Chemistry and possibly add a link to a new quizzo form)

4. Inspired
This page is like a blog page where we can upload videos, links to articles that we find to be inspiring and hopefully will inspire others.

5. Inspire
This is a recruitment page. Only content here.

6. Contact us.
Mapzy map widget and a 'contact us' form

* Our branding requires green close to #12FF3D

***Please have a look at the current website.
@ www.brindlelearning.com.au

Thanks everybody hope the revision of my brief is better and more informative than my last one

Target Market(s)

senior highschool students aged 15-19, parents ( to a lesser degree)

Industry/Entity Type

It Company

Requirements
Must have
• Ability to change content on pages.

The green doesn't have to be everywhere, but it must be obvious that it is our colour.

Nice to have
• Sites with a nicer mix of images and flash will be given more consideration. But then again, if you amaze us, you amaze us and we will go with your design.
Should not have
• Should stay away from ocre, brown colours and serif fonts.

```html
<!DOCTYPE html>
<html lang="en">
<head>
<meta charset="utf-8">
<title>Brindle Learning – real HSC coaching &amp; mentoring</title>
<link rel="stylesheet" href="https://fonts.googleapis.com/css2?family=Delius&family=Open+Sans:ital,wght@0,400;0,700;1,400&display=swap">
<style>
:root{
  --brand:#14f535;
  --brand-soft:#8ef79d;
  --page:#f3f3f2;
  --ink:#333;
  --muted:#555;
  --soft:#9a9a9a;
  --white:#fff;
  --highlight:#fff200;
  --rule:#c9c9c9;
  --frame:#c9434b;
  --tweet-top:#e9f6fc;
  --tweet-bottom:#9fd7ef;
  --link:#3b5998;
}
*{box-sizing:border-box;margin:0;padding:0}
html,body{width:708px;height:1200px;overflow:hidden}
body{position:relative;background:var(--page);font-family:"Open Sans",Arial,sans-serif;color:var(--ink)}
a{text-decoration:none}

/* header */
.site-header{position:absolute;left:0;top:0;width:708px;height:55px;background:var(--brand)}
.brand{position:absolute;left:72px;top:17px;display:flex;align-items:center;gap:6px;color:var(--white);font-family:"Delius",Arial,sans-serif;font-size:14px;line-height:1}
.brand-mark{width:18px;height:18px;background:var(--white)}
.main-nav{position:absolute;right:70px;top:20px;display:flex;gap:17px;font-family:"Delius",Arial,sans-serif;font-size:13.5px;color:var(--white);white-space:nowrap}

/* hero */
.hero-frame{position:absolute;left:75px;top:94px;width:343px;height:234px;background:var(--white);border:1px solid #ddd;box-shadow:0 1px 3px rgba(0,0,0,.15);transform:rotate(-.6deg)}
.hero-photo{position:absolute;left:79px;top:100px;width:335px;height:221px;background:linear-gradient(135deg,#f3e6c3,#c98f5a 45%,#6fbf6a 70%,#4aa9c9)}
.hero-copy{position:absolute;left:449px;top:114px;width:192px}
.hero-copy h1{font-family:"Delius",Arial,sans-serif;font-weight:400;font-size:21px;line-height:26px;color:#333}
.hero-copy h2{font-family:"Delius",Arial,sans-serif;font-weight:400;font-size:13px;line-height:18px;color:#444;white-space:nowrap}
.hero-copy p{font-size:9.1px;line-height:16px;color:var(--muted);margin-top:14px;letter-spacing:-.05px}
.hero-copy mark{background:var(--highlight);color:var(--muted)}
.btn{position:absolute;height:21px;padding:0 13px;background:var(--brand);color:var(--white);font-family:"Delius",Arial,sans-serif;font-size:11px;line-height:21px;border-radius:4px;display:flex;align-items:center;gap:5px;white-space:nowrap}
.btn svg{display:block}

.divider{position:absolute;left:71px;width:566px;border-top:2px dashed var(--rule)}

.section-title{position:absolute;font-family:"Delius",Arial,sans-serif;font-weight:400;font-size:16px;color:#333;white-space:nowrap}

.photo-card{position:absolute;background:var(--white);border:1px solid #ccc;padding:3px}
.photo-fill{width:100%;height:100%}
.trial-copy{position:absolute;left:183px;top:436px;width:152px;font-size:9.4px;line-height:15px;color:var(--muted)}

.quote-box{position:absolute;left:375px;top:437px;width:260px;height:106px;background:var(--white);box-shadow:3px 3px 0 #d6d6d6;border-top:1px solid #ccc}
.quote-box blockquote{position:absolute;left:15px;top:14px;width:232px;font-family:"Delius",Arial,sans-serif;font-style:italic;font-size:10px;line-height:16px;color:#555}
.quote-box cite{position:absolute;right:16px;top:81px;font-style:normal;font-weight:700;font-size:9px;color:#555}

/* news */
.news-item{position:absolute;left:71px;width:375px;height:70px}
.news-thumb{position:absolute;left:0;top:0;width:66px;height:64px;background:var(--white);border:1px solid #ccc;padding:2px}
.news-item h3{position:absolute;left:73px;top:1px;font-family:"Delius",Arial,sans-serif;font-weight:400;font-size:11px;color:#222;white-space:nowrap}
.news-item time{position:absolute;left:73px;top:16px;font-style:italic;font-size:7px;color:var(--soft)}
.news-item p{position:absolute;left:73px;top:28px;width:302px;font-size:8.3px;line-height:13px;color:#333;letter-spacing:-.05px}

.newsletter{position:absolute;left:473px;top:659px;width:164px;height:141px;background:var(--white);border:3px solid var(--frame)}
.newsletter h4{position:absolute;left:16px;top:20px;font-size:11.5px;font-weight:700;color:#222;letter-spacing:.2px}
.newsletter p{position:absolute;left:16px;top:37px;width:140px;font-family:"Delius",Arial,sans-serif;font-size:9.4px;line-height:13px;color:#333}
.newsletter .field{position:absolute;left:16px;top:69px;width:128px;height:20px;border:1px solid #555;border-radius:3px;font-style:italic;font-size:7.5px;color:#999;padding:5px 6px}

/* footer */
.site-footer{position:absolute;left:0;top:854px;width:708px;height:346px;background:var(--brand)}
.footer-ornament{position:absolute;left:71px;top:854px;width:566px;height:72px;background:linear-gradient(var(--page),var(--brand-soft) 55%,var(--brand))}
.map{position:absolute;left:71px;top:941px;width:166px;height:86px;border:3px solid var(--white);border-radius:3px;background:linear-gradient(160deg,#ece9e1,#e2dfd6 50%,#f2e8a8)}
.contact{position:absolute;left:71px;top:1038px;font-style:normal;font-size:8.6px;line-height:13px;color:#111}
.contact strong{display:block;font-family:"Delius",Arial,sans-serif;font-weight:400;font-size:11px;margin-bottom:2px}
.social-box{position:absolute;left:271px;top:940px;width:168px;height:151px;background:var(--white);border:1px solid #ccc;border-top:2px solid var(--link)}
.social-box .page-name{position:absolute;left:38px;top:6px;font-size:8.6px;font-weight:700;color:var(--link)}
.social-box .page-sq{position:absolute;left:9px;top:9px;width:22px;height:22px;background:var(--brand)}
.social-box .like{position:absolute;left:38px;top:20px;border:1px solid #ccc;background:#f5f5f5;font-size:6.5px;padding:1px 4px;color:#444}
.social-box .count{position:absolute;left:6px;top:44px;font-size:6.3px;color:#333;border-top:1px solid #ddd;width:154px;padding-top:4px}
.social-box .count b{color:var(--link);font-weight:400}
.faces{position:absolute;left:6px;top:58px;display:grid;grid-template-columns:repeat(4,29px);gap:3px}
.faces span{height:29px;background:linear-gradient(160deg,#b9b4c9,#4b4350)}
.social-box .plugin{position:absolute;left:6px;top:128px;width:154px;border-top:1px solid #ddd;padding-top:4px;font-size:5.8px;color:var(--link);display:flex;gap:3px;align-items:center}
.social-box .plugin i{width:7px;height:7px;background:var(--link);display:block}
.tweet{position:absolute;left:473px;top:941px;width:164px;height:91px;border-radius:5px;border:1px solid #8ec9e4;background:linear-gradient(var(--tweet-top),var(--tweet-bottom));padding:10px 12px;font-size:8.2px;line-height:12.5px;color:#333}
.tweet em{font-size:6.5px;text-decoration:underline}
.tweet-tail{position:absolute;left:570px;top:1031px}
.follow-art{position:absolute;left:596px;top:1013px;width:40px;height:46px;border-radius:6px;background:linear-gradient(160deg,#c24e16,#3aa8e0)}
.follow-btn{position:absolute;left:553px;top:1066px;width:84px;height:13px;background:var(--white);border:1px solid #bbb;border-radius:3px;font-size:5.3px;font-weight:700;color:#333;display:flex;align-items:center;gap:3px;padding-left:4px;white-space:nowrap}
.follow-btn i{width:6px;height:6px;border-radius:50%;background:#38a6df;display:block;flex:none}
.foot-rule{position:absolute;left:71px;top:1127px;width:566px;border-top:2px dashed rgba(255,255,255,.8)}
.foot-nav{position:absolute;left:0;top:1140px;width:708px;display:flex;justify-content:center;gap:14px;font-family:"Delius",Arial,sans-serif;font-size:10.5px;color:var(--white)}
.foot-icons{position:absolute;left:0;top:1157px;width:708px;display:flex;justify-content:center;gap:4px}
.foot-icons span{width:12px;height:12px;border-radius:50%;background:var(--white)}
.copyright{position:absolute;left:0;top:1177px;width:708px;text-align:center;font-size:7px;color:var(--white)}
</style>
</head>
<body>

<header class="site-header">
  <div class="brand"><span class="brand-mark"></span>Brindle Learning</div>
  <nav class="main-nav">
    <span>About Us</span><span>Courses</span><span>Inspired</span><span>Inspire</span><span>Contact Us</span>
  </nav>
</header>

<main>
  <div class="hero-frame"></div>
  <div class="hero-photo" role="img" aria-label="Photo of a smiling group of senior high school students holding books"></div>

  <section class="hero-copy">
    <h1>I am Brindle</h1>
    <h2>real HSC coaching &amp; mentoring</h2>
    <p>The HSC help you need, in the years you need it. We offer <mark>small classes, individualised attention and genuine care</mark> for each student. It's different - in a good way. Please let us know if there's any way we can help you on your journey.</p>
  </section>
  <a class="btn" style="left:449px;top:287px">find out more
    <svg width="10" height="8" viewBox="0 0 10 8"><path d="M0 3h6V0l4 4-4 4V5H0z" fill="#fff"/></svg></a>

  <div class="divider" style="top:369px"></div>

  <h2 class="section-title" style="left:71px;top:407px">FREE Trial Lesson</h2>
  <div class="photo-card" style="left:71px;top:436px;width:103px;height:118px">
    <div class="photo-fill" role="img" aria-label="Photo of a tutor helping a student at a desk" style="background:linear-gradient(150deg,#e9d7b5,#a8744e 55%,#5a3b2a)"></div>
  </div>
  <p class="trial-copy">Because we believe you shouldn't have to sign up until you see what it's actually like. Enquire us today to ask for your FREE trial lesson!</p>
  <a class="btn" style="left:183px;top:513px">enquire now
    <svg width="10" height="8" viewBox="0 0 10 8"><path d="M0 3h6V0l4 4-4 4V5H0z" fill="#fff"/></svg></a>

  <h2 class="section-title" style="left:375px;top:407px">What Our Students Say</h2>
  <figure class="quote-box">
    <blockquote>I like the teachers and that we can study there; it's comfortable. They don't help you just with study, but other things too, and it's really easy to ask the teachers questions about stuff you don't know.</blockquote>
    <cite>— JT, Kestrel Grove</cite>
  </figure>

  <div class="divider" style="top:592px"></div>

  <h2 class="section-title" style="left:71px;top:629px">Latest News</h2>

  <article class="news-item" style="top:659px">
    <div class="news-thumb"><div class="photo-fill" role="img" aria-label="Workshop flyer thumbnail" style="background:linear-gradient(#1d2a1d,#2f6a2a)"></div></div>
    <h3>Year 11 FREE HSC Workshops!</h3>
    <time>September 12, 2012</time>
    <p>This is a great opportunity to get prepared for your HSC year. To register for the FREE English and/or 3U Maths workshops, or for our Chemistry Intensive these holidays, send us your name, phone number and the...</p>
  </article>

  <article class="news-item" style="top:750px">
    <div class="news-thumb"><div class="photo-fill" role="img" aria-label="Photo of a university building column" style="background:linear-gradient(#b7a98f,#6f6252)"></div></div>
    <h3>Uni Open Days 2012</h3>
    <time>August 20, 2012</time>
    <p>Many students are thrown into near-despair over their QAB preferences. Everywhere we go we hear the moan, “I just wish I knew what I wanted to do!” But in reality, it's tough to figure out what you want to do for...</p>
  </article>

  <aside class="newsletter">
    <h4>NEWSLETTER</h4>
    <p>Subscribe to receive our latest news and offers!</p>
    <div class="field">Your email?</div>
    <a class="btn" style="left:16px;top:99px">sign up
      <svg width="10" height="8" viewBox="0 0 10 8"><path d="M0 3h6V0l4 4-4 4V5H0z" fill="#fff"/></svg></a>
  </aside>
</main>

<footer>
  <div class="site-footer"></div>
  <div class="footer-ornament" role="img" aria-label="Decorative band of speech bubbles along the top of the footer"></div>

  <div class="map" role="img" aria-label="Mapzy map showing the centre's street location"></div>
  <address class="contact">
    <strong>Brindle Learning</strong>
    Visit: 42 Larkin St Hazelmere NSW 2199<br>
    Call: (02) 5550 1290<br>
    Email: learn@brindlelearning.com.au
  </address>

  <div class="social-box">
    <span class="page-sq"></span>
    <span class="page-name">brindle learning</span>
    <span class="like">Like</span>
    <p class="count">1,744,476 people like <b>brindle learning</b></p>
    <div class="faces" role="img" aria-label="Grid of follower profile photos">
      <span></span><span></span><span></span><span></span>
      <span></span><span></span><span></span><span></span>
    </div>
    <p class="plugin"><i></i>chatterbook social plugin</p>
  </div>

  <div class="tweet">Dolor sit amet, consectetur adipiscing elit. Nam ut metus ligula, nec consectetur orci maecenas tempor aliquam svelit dol. <em>5 hours ago</em></div>
  <svg class="tweet-tail" width="20" height="14" viewBox="0 0 20 14" aria-hidden="true"><path d="M0 0h20L14 14z" fill="#9fd7ef"/></svg>
  <div class="follow-art" role="img" aria-label="Follow me sign illustration"></div>
  <div class="follow-btn"><i></i>Follow @brindlelearning</div>

  <div class="foot-rule"></div>
  <nav class="foot-nav"><span>Home</span><span>About Us</span><span>Courses</span><span>Inspired</span><span>Inspire</span><span>Contact Us</span></nav>
  <div class="foot-icons" aria-label="Social links"><span></span><span></span><span></span><span></span><span></span><span></span></div>
  <p class="copyright">©2013 brindle learning. All rights reserved.</p>
</footer>

</body>
</html>
```